Traineeship Flyer Design Project

Requirements:
• 1 x A4 page flyer (double sided)
1st page; target market 15-19 yr old, looking for young/fresh, exciting, eye catching
2nd page: same look/feel – target market – parents/person to determine if there is value to devoting energy to this qualification (potentially less busy in design)
• Use of high quality logos: 1. Kestravo 2. Nationally recognised training logo
Ideally wanting to keep amount of copy to the page layout as attached, although designer is free to interpret the layout of copy on each page, although Kestravo will accept alternative presentation if designer sees new way to combine information
• Kestravo does not have a set colour palette so there are no restrictions/guidelines to follow
Updates
Hi, All files including brief and logos have now been updated.
Reason: Hi everyone
Please refer to design submission below for the only design that was deemed to cover off on the brief as the starting point - in regards to producing a design that appeals to target market of young person (15-19) in regards to self selecting to take up further study
Hi everyone
Can you please view the 3 remaining designs that are in contention (out of 30+ submitted) - Design 1528020 ; 1510098; 1510087; I will be providing additional feedback to these designers, as that come closer to the mark of appealing to younger "potential trainee" - the collateral needs to make the young student want to pick up the flyer (eye catching/interesting) and then be motivated to want to self elect - "beg parents" to take up the option. **PLEASE NOTE - I have uploaded a colour swatch now, and would appreciate if desgins could use these colours (not a requirement to use base colours of blue a silver as base if an exciting image needs to come from leaning on "secondary colours" (brighter) as being the predominant colours.
Many thanks, appreciate being able to see such an active community of designers involved in this website
Target Market(s)
1st page; target market 15-19 yr old, looking for young/fresh, exciting, eye catching. same look/feel – target market – parents/person to decide on
Industry/Entity Type
Training
Look and feel
Each slider illustrates characteristics of the customer's brand and the style your logo design should communicate.

```html
<!DOCTYPE html>
<html lang="en">
<head>
<meta charset="utf-8">
<title>Traineeship Flyer – Kestravo</title>
<link href="https://fonts.googleapis.com/css2?family=Open+Sans:wght@400;600;700;800&family=Kalam:wght@400;700&display=swap" rel="stylesheet">
<style>
:root{
  --navy:#1c3768;
  --green:#46a537;
  --green-band:#8cc63f;
  --blue-band:#2aa9e0;
  --orange-band:#f7931e;
  --purple-band:#8d8fca;
  --text:#3a3a3a;
  --white:#ffffff;
}
*{margin:0;padding:0;box-sizing:border-box}
html,body{width:848px;height:1200px;overflow:hidden;background:var(--white)}
body{font-family:"Open Sans",Arial,sans-serif;color:var(--text);position:relative}
.flyer{position:relative;width:848px;height:1200px;overflow:hidden}

.masthead{position:absolute;left:0;top:0;width:848px;height:100px;background:var(--navy);color:var(--white);text-align:center;padding-top:12px}
.masthead h1{font-size:31px;font-weight:800;letter-spacing:.2px;line-height:38px}
.masthead p{font-size:24px;font-weight:700;line-height:32px}

.info{position:absolute}
.info h2{color:var(--green);font-size:20px;font-weight:700;line-height:24px;margin-bottom:5px}
.info p{font-size:14px;line-height:19px}
.info ul{list-style:none;font-size:14px;line-height:20px}
.info li::before{content:"• ";}

.paid-time{position:absolute;left:440px;top:240px;display:flex;align-items:center;gap:14px}
.paid-time .people{width:88px;height:58px;background:#e4eef7;border-radius:6px}
.paid-time p{font-family:"Kalam",cursive;color:var(--green);font-size:27px;line-height:28px;font-weight:400}

.band{position:absolute;left:0;width:848px}
.band svg.shape{position:absolute;left:0;top:0}
.band .icon{position:absolute;left:36px;width:72px;height:72px;border-radius:8px;background:rgba(255,255,255,.35)}
.band .content{position:absolute;left:155px;right:30px}
.band h3{color:var(--navy);font-size:21px;font-weight:700;line-height:27px}
.band .row{font-size:14px;font-weight:700;color:var(--navy);line-height:24px}
.band .sep{color:var(--white);font-weight:800;margin:0 5px}

.quals{display:flex;gap:10px;margin-top:12px;align-items:flex-start}
.qual{font-size:14px;line-height:18px;color:var(--navy)}
.qual b{display:block;font-weight:800}
.qual span{display:block;font-weight:600;color:#ffffff}
.qual .code{color:var(--navy);font-weight:400}
.quals .arrow{color:var(--white);font-size:24px;font-weight:800;line-height:22px}

.reasons{list-style:none;margin-top:8px}
.reasons li{font-size:14px;line-height:22px;color:var(--navy);display:flex;gap:8px}
.reasons .num{font-family:"Kalam",cursive;color:var(--white);font-size:22px;width:14px;line-height:22px}

.more{position:absolute;top:912px}
.more h2{color:var(--green);font-size:20px;font-weight:700;line-height:26px;margin-bottom:4px}
.more p{font-size:14px;line-height:19px;text-align:justify}
.more p.small{font-size:12px;line-height:16px;margin-top:10px}
.rto{display:flex;align-items:flex-end;gap:20px;margin-top:12px;font-size:11px}
.rto .badge{width:60px;height:32px;background:#cfd6de;border-radius:3px}

.footer{position:absolute;left:0;bottom:0;width:848px;height:50px;background:var(--navy);color:var(--white);font-size:24px;font-weight:700;text-align:center;line-height:50px}
</style>
</head>
<body>
<main class="flyer">

  <header class="masthead">
    <h1>GAIN A FORMAL NATIONAL QUALIFICATION</h1>
    <p>Recognised by all employers Australia wide</p>
  </header>

  <section class="info" style="left:34px;top:116px;width:384px">
    <h2>How much will it cost?</h2>
    <p>Nothing! The full course is provided by your employer.<br>No prior training/experience is required.</p>
    <h2 style="margin-top:14px">How long will it take to finish my traineeship?</h2>
    <p style="text-align:justify">If you remain on track, you could complete a Cert II in 6 months or a Cert III in 7 months. Don’t worry, a dedicated Trainer is committed to making your training a fun, informative and worthwhile experience.</p>
  </section>

  <section class="info" style="left:438px;top:116px;width:390px">
    <h2>What would I be expected to do?</h2>
    <ul>
      <li>Earn while your learn</li>
      <li>Attend on site training sessions</li>
      <li>Online training and assessment</li>
      <li>Complete workplace activities</li>
    </ul>
  </section>

  <div class="paid-time">
    <div class="people" role="img" aria-label="Small group of trainee figures"></div>
    <p>All training completed<br>during paid work time!</p>
  </div>

  <section class="band" style="top:332px;height:156px">
    <svg class="shape" width="848" height="156" viewBox="0 0 848 156"><polygon points="6,6 834,0 842,150 10,156" fill="var(--blue-band)"/></svg>
    <div class="icon" style="top:40px" role="img" aria-label="Form icon"></div>
    <div class="content" style="top:14px">
      <h3>SIGN UP TODAY for the opportunity to complete one<br>of these qualifications:</h3>
      <div class="quals">
        <div class="qual"><b>CERTIFICATE II</b><span>Retail Services</span><span class="code">(SIR20212)</span></div>
        <div class="arrow">&gt;</div>
        <div class="qual"><b>CERTIFICATE III</b><span>Retail Operations</span><span class="code">(SIR30212)</span></div>
        <div class="arrow">&gt;</div>
        <div class="qual"><b>CERTIFICATE IV</b><span>Frontline<br>Management</span><span class="code">(BSB40807)</span></div>
        <div class="arrow">&gt;</div>
        <div class="qual"><b>DIPLOMA OF MANAGEMENT</b><span>Business</span><span class="code">(BSB51107)</span></div>
      </div>
    </div>
  </section>

  <section class="band" style="top:488px;height:176px">
    <svg class="shape" width="848" height="176" viewBox="0 0 848 176"><polygon points="8,4 712,0 716,170 4,176" fill="var(--green-band)"/></svg>
    <div class="icon" style="top:52px" role="img" aria-label="Checklist icon"></div>
    <div class="content" style="top:14px">
      <h3>5 GREAT REASONS to complete a Traineeship:</h3>
      <ol class="reasons">
        <li><span class="num">1</span>It’s a formal qualification; Recognised nationally; Equivalent to attending TAFE</li>
        <li><span class="num">2</span>No formal ‘exams’ : Complete workbooks, online and practical tasks instead</li>
        <li><span class="num">3</span>Supercharge your resume, stand out from the crowd</li>
        <li><span class="num">4</span>Learn new skills with people you work with, in the comfort of your workplace</li>
        <li><span class="num">5</span>Earn while you learn</li>
      </ol>
    </div>
  </section>

  <section class="band" style="top:664px;height:128px">
    <svg class="shape" width="848" height="128" viewBox="0 0 848 128"><polygon points="4,6 842,0 836,124 10,128" fill="var(--orange-band)"/></svg>
    <div class="icon" style="top:28px" role="img" aria-label="Open box icon"></div>
    <div class="content" style="top:12px">
      <h3>TOPICS COVERED in your qualification which teach<br>transferable skills may include:</h3>
      <div class="row" style="margin-top:8px">Customer service<span class="sep">&gt;</span>Merchandising<span class="sep">&gt;</span>Teamwork/Communication<span class="sep">&gt;</span>Finance</div>
      <div class="row">Safety/Security<span class="sep">&gt;</span>Manage Sales and Service<span class="sep">&gt;</span>Marketing<span class="sep">&gt;</span>Goal Setting<span class="sep">&gt;</span>Food Safety</div>
    </div>
  </section>

  <section class="band" style="top:798px;height:108px">
    <svg class="shape" width="848" height="108" viewBox="0 0 848 108"><polygon points="6,0 836,6 830,106 4,108" fill="var(--purple-band)"/></svg>
    <div class="icon" style="top:18px" role="img" aria-label="Light bulb icon"></div>
    <div class="content" style="top:14px">
      <h3>EXCELLENT possible career choices:</h3>
      <div class="row" style="margin-top:6px">Senior Sales Assistant<span class="sep">&gt;</span>Shift Manager<span class="sep">&gt;</span>Human Resources</div>
      <div class="row">Merchandise Manager<span class="sep">&gt;</span>Customer Service Manager<span class="sep">&gt;</span>Small Business Retail Owner</div>
    </div>
  </section>

  <section class="more" style="left:34px;width:384px">
    <h2>What if I am at school?</h2>
    <p>School based Traineeships provide credit towards your secondary school certificate. Schools and employers will work together to provide you with the best options.</p>
    <h2 style="margin-top:12px">Am I eligible?</h2>
    <p>The government has strict criteria for Traineeships, which varies in each state. Submit your expression of interest and your application will be reviewed to determine your eligibility.</p>
  </section>

  <section class="more" style="left:438px;width:384px;top:906px">
    <h2>Who provides the training?</h2>
    <p>Kestravo is an award winning national registered training organisation with over 14 years experience.</p>
    <p class="small">Kestravo encourages participation of learners with physical or mental disabilities in supporting the Equal Opportunity Act 1995 and other laws. Government Funding is also available in some states for this program. If you have any further questions about Traineeships, please contact your local Kestravo Training office on the details below.</p>
    <div class="rto"><span>RTO ID| 4417</span><div class="badge" role="img" aria-label="Training accreditation badge"></div></div>
  </section>

  <footer class="footer">www.kestravo.com.au &nbsp;|&nbsp; 1300 555 018 &nbsp;|&nbsp; info@kestravo.com.au</footer>

</main>
</body>
</html>
```